I have a new startup... www.hirewithplindle.com
An issue Im running into is when people create profiles there banner images are getting messed up. So instead I would like anywhere to 10-15 banners created as stock banners for my site the people signing up need to choose from so the website looks more in uniform. The site contains graphic designers, photographers, & videographers so maybe some banners can be patterns of a camera outline or graphic design tools etc. Need really clean and sleek looking banners that these people can pick from that will make sense.
I will attach my logo if you want to do a cool "Plindle" pattern design as a banner.
Banner sizes 2000px by 560px.

If you have any questions please let me know.

```html
<!DOCTYPE html>
<html lang="en">
<head>
<meta charset="UTF-8">
<title>Plindle Banner – Event Videography</title>
<link rel="stylesheet" href="https://fonts.googleapis.com/css2?family=Montserrat:wght@800&display=swap">
<style>
  :root {
    --brand-rust: #c44b2a;
    --paper-white: #ffffff;
    --photo-dark: #2b2523;
    --photo-shadow: #4a3f39;
    --photo-brown: #8a7258;
    --photo-warm-mid: #c9ae86;
    --photo-warm-light: #e8dcc6;
    --photo-cream: #f3ece0;
    --photo-teal: #5f7a76;
  }
  * { margin: 0; padding: 0; box-sizing: border-box; }
  html, body {
    width: 1200px;
    height: 336px;
    overflow: hidden;
    background: var(--paper-white);
  }
  .banner {
    position: relative;
    width: 1200px;
    height: 336px;
    overflow: hidden;
  }
  .banner__photo {
    position: absolute;
    inset: 0;
    background:
      linear-gradient(90deg, rgba(95,122,118,0) 54%, rgba(95,122,118,0.45) 58%, rgba(95,122,118,0.1) 63%, rgba(95,122,118,0) 66%),
      linear-gradient(90deg,
        var(--photo-dark) 0%,
        var(--photo-dark) 18%,
        var(--photo-shadow) 27%,
        var(--photo-brown) 35%,
        var(--photo-warm-mid) 44%,
        var(--photo-warm-light) 60%,
        var(--photo-warm-mid) 72%),
      var(--photo-warm-mid);
  }
  .banner__photo::after {
    content: "";
    position: absolute;
    inset: 0;
    background: linear-gradient(180deg, rgba(120,95,65,0.25) 0%, rgba(255,255,255,0) 45%, rgba(243,236,224,0.35) 100%);
  }
  .banner__shape {
    position: absolute;
    inset: 0;
    width: 1200px;
    height: 336px;
  }
  .banner__brand {
    position: absolute;
    left: 739px;
    width: 408px;
    top: 100px;
    height: 90px;
    display: flex;
    align-items: center;
    justify-content: center;
    font-family: "Montserrat", sans-serif;
    font-weight: 800;
    font-size: 100px;
    letter-spacing: -3px;
    line-height: 1;
    color: var(--paper-white);
    text-transform: uppercase;
    white-space: nowrap;
  }
</style>
</head>
<body>
  <div class="banner">
    <div class="banner__photo" role="img" aria-label="Photo of a video camera with its flip-out screen open, filming a decorated banquet hall with white-covered chairs and tables in warm light"></div>

    <svg class="banner__shape" viewBox="0 0 1200 336" aria-hidden="true">
      <path d="M632 0 C620 40 616 120 630 180 C648 250 700 308 756 336 L1200 336 L1200 0 Z" fill="var(--brand-rust)"/>
      <path d="M735 0 C690 50 660 120 664 175 C668 240 708 298 752 336" fill="none" stroke="var(--paper-white)" stroke-width="3"/>
    </svg>

    <div class="banner__brand">Plindle</div>
  </div>
</body>
</html>
```